PACKAGE DESIGN - Candies - yum!!

I have added a photo below of another product. The element we like is the "stripes" through the packaging. We would like you to consider this element.
Good day all!
Our product is a candy coated chocolate. You'd know them as Q&Z's or Bolvicks (not the US version of it, but the one everywhere else).
They are small, 1cm diameter. They are available in a bunch of colors. And they are very very tasty!
Need:
(1) One BASE design
(2) 2 different background versions of it (colors) - but we will leave that up to you
(3) the package should be BRIGHT . likely we will make it very glossy.
(4) its a kids product, not some sort of dark chocolate from some obscure plantation in some organic zero emission area. Its just fun chocolate!
(5) we do NOT need a mascot. We want only the product featured and the name
(6) at least ONE of the products has to be broken/open in order to show that its chocolate filled.
PRODUCT NAME:
"ZIG ON!"
Colors of the candy (outside):
Red
Purple
Yellow
Green
Blue
Brown
Package Dimensions:
16cm long
7cm high
This should be an easy one! no mascot and simple elliptical multi color candies!
Once we have narrowed down to 2-3 final designs we will ask for slogan etc to be put in.
After we select the winner, we will ask for some small assistance to pie up the package with bar codes etc
Target Market(s)
Kids!
Industry/Entity Type
Product
Requirements
Must have
- MUST HAVE FUN!
If you need some ideas, please look up
"Varbo Bolvicks" on google images.
Q&Zs packaging is too mature for our taste. Something in between the two.
The product will look 90% similar to an Q&Z. 1cm diameter and about 5mm high.

```html
<!DOCTYPE html>
<html lang="en">
<head>
<meta charset="utf-8">
<title>ZIG ON – Chocolate Candy Package</title>
<link rel="stylesheet" href="https://fonts.googleapis.com/css2?family=Fredoka:wght@700&family=Crimson+Text&display=swap">
<style>
  :root {
    --sky-violet: #5b45a0;
    --deep-violet: #4a3a92;
    --band-ice: #d4ebf8;
    --band-magenta: #b0338f;
    --band-plum: #8a3d98;
    --band-cyan: #19a6e0;
    --band-indigo: #3b3a8c;
    --chocolate: #3e2416;
    --title-purple: #8b2a98;
    --candy-yellow: #f6c21c;
    --candy-blue: #1aa0e0;
    --candy-green: #3db54a;
    --candy-pink: #e2188f;
    --candy-brown: #6b3a1c;
    --label-white: #ffffff;
  }
  html, body {
    margin: 0;
    padding: 0;
    overflow: hidden;
    background: #ffffff;
  }
  .package {
    position: relative;
    width: 1200px;
    height: 523px;
    overflow: hidden;
    background: linear-gradient(90deg, var(--sky-violet), var(--deep-violet));
  }
  .stripes, .candies {
    position: absolute;
    inset: 0;
    width: 1200px;
    height: 523px;
  }
  .brand-name {
    position: absolute;
    left: 60px;
    top: 70px;
    margin: 0;
    font-family: "Fredoka", sans-serif;
    font-weight: 700;
    font-size: 290px;
    line-height: 1;
    letter-spacing: 4px;
    color: var(--title-purple);
    white-space: nowrap;
  }
  .product-type {
    position: absolute;
    left: 751px;
    top: 420px;
    margin: 0;
    font-family: "Crimson Text", serif;
    font-size: 27px;
    color: var(--label-white);
  }
</style>
</head>
<body>
<main class="package">
  <svg class="stripes" viewBox="0 0 1200 523" aria-hidden="true">
    <path fill="var(--band-ice)" d="M0 0H1200V40C1000 70 880 10 700 30C520 50 420 80 250 60C130 45 60 70 0 80Z"/>
    <path fill="var(--band-plum)" d="M0 95C90 80 170 70 300 90C460 115 560 70 720 55C880 40 1000 80 1200 50V95C1000 125 880 90 720 100C560 110 460 150 300 135C170 120 90 130 0 145Z"/>
    <path fill="var(--band-ice)" d="M0 155C100 140 200 140 320 160C470 185 580 130 740 120C900 110 1020 140 1200 115V140C1020 170 900 140 740 150C580 160 470 215 320 195C200 180 100 185 0 200Z"/>
    <path fill="var(--band-magenta)" d="M0 200C120 190 220 195 340 210C480 228 600 185 760 170C920 155 1040 170 1200 150V172C1040 195 920 180 760 195C600 210 480 250 340 235C220 222 120 215 0 225Z"/>
    <path fill="var(--band-cyan)" d="M0 240C120 230 230 235 350 250C500 268 620 225 780 210C940 195 1060 205 1200 190V215C1060 232 940 222 780 238C620 254 500 295 350 280C230 268 120 262 0 270Z"/>
    <path fill="var(--band-indigo)" d="M0 290C130 280 240 290 360 305C510 322 630 285 800 268C960 252 1070 262 1200 245V300C1070 315 960 305 800 322C630 340 510 375 360 360C240 348 130 340 0 350Z"/>
    <path fill="var(--band-ice)" d="M0 360C130 350 250 360 380 375C520 390 650 360 820 345C980 330 1080 330 1200 320V345C1080 355 980 355 820 372C650 390 520 418 380 402C250 388 130 380 0 392Z"/>
    <path fill="var(--band-plum)" d="M0 405C140 395 260 405 400 418C540 430 680 405 840 392C1000 380 1100 378 1200 370V400C1100 408 1000 410 840 422C680 435 540 458 400 448C260 438 140 430 0 440Z"/>
    <path fill="var(--chocolate)" d="M0 462C200 452 400 458 600 455C800 452 1000 450 1200 452V523H0Z"/>
  </svg>

  <h1 class="brand-name">ZIG ON</h1>

  <svg class="candies" viewBox="0 0 1200 523">
    <circle role="img" aria-label="Yellow candy" cx="185" cy="198" r="50" fill="var(--candy-yellow)"/>
    <circle role="img" aria-label="Blue candy" cx="578" cy="205" r="50" fill="var(--candy-blue)"/>
    <circle role="img" aria-label="Green candy" cx="1070" cy="139" r="27" fill="var(--candy-green)"/>
    <circle role="img" aria-label="Green candy" cx="1130" cy="119" r="32" fill="var(--candy-green)"/>
    <circle role="img" aria-label="Pink candy" cx="640" cy="420" r="36" fill="var(--candy-pink)"/>
    <circle role="img" aria-label="Brown candy" cx="710" cy="426" r="40" fill="var(--candy-brown)"/>
  </svg>

  <p class="product-type">Chocolate Candy</p>
</main>
</body>
</html>
```